Postcard Design

Heating & Cooling

I want to create a post card for a Tune Up program that we offer customer for this spring.
Updates

I would like to change the date from April 1st - June 31st.
I would also like to change the size and go larger for the post card.

Keep the designs coming.
Thanks

I have decided to change the price of the cost of the program to "Only $99.00" due to other competitors pricing in my area.
If possible include at the bottom of the design > "Does not cover repair or parts" in a small font

Reason: We need more time for better designs. So I am extending the deadline by 7 days.

Target Market(s)

Residential Customers for Air Conditioning Tune Ups

Requirements
Must have
• We are promoting a tune up for the air conditioning system for $129.00.

The price is effective from April 1st - July 31st

I would like for the post card to be attention grabbing from the customers point of view. So mainly, add bold letting and everything to get attention.
Nice to have
• Also add to the card if possible:
Lower Energy Bills
Increase the life of your system
Prevent future breakdowns

Stay Cool this Summer with our Brightvale Tune Up Program

And add a logo that shows stacks of coins to indicate the money that can be saved

You also can look at other post cards that has been created for this particular program and design from it.

```html
<!DOCTYPE html>
<html lang="en">
<head>
<meta charset="utf-8">
<title>Brightvale Tune-Up Postcard</title>
<link rel="stylesheet" href="https://fonts.googleapis.com/css2?family=Anton&family=Archivo+Black&family=Fira+Sans+Extra+Condensed:ital,wght@1,600&family=Open+Sans:ital,wght@0,400;0,700;1,600&family=Oswald:wght@600&display=swap">
<style>
  :root{
    --page:#f2f2f2;
    --ink:#111111;
    --red:#d01f2b;
    --ribbon:#e52629;
    --band:#174f66;
    --tick:#6db3e3;
    --grey:#6b6b6b;
  }
  *{margin:0;padding:0;box-sizing:border-box}
  html,body{width:1200px;height:1075px;overflow:hidden;background:var(--page)}
  .postcard{
    position:absolute;left:40px;top:104px;width:1120px;height:867px;overflow:hidden;
    background:linear-gradient(100deg,#ffffff 0%,#ffffff 35%,#e6f3fb 65%,#cfe8f8 100%);
  }
  .swoosh{position:absolute;left:0;top:0;width:1120px;height:867px}
  .photo{
    position:absolute;left:43px;top:280px;width:404px;height:481px;
    background:linear-gradient(180deg,#c9d4e6 0%,#93a7c8 45%,#2b2f3a 75%,#c4c0b6 100%);
  }
  .badge{position:absolute;left:3px;top:0;width:333px;height:331px}
  .badge-title{
    position:absolute;left:0;top:18px;width:330px;text-align:center;
    font:400 42px/50px "Archivo Black",sans-serif;color:var(--ink);letter-spacing:-.5px;
  }
  .badge-ribbon{
    position:absolute;left:44px;top:133px;width:242px;height:84px;
    display:flex;align-items:center;justify-content:center;
    font:600 36px/1 "Oswald",sans-serif;color:#fff;
  }
  .badge-note{
    position:absolute;left:118px;top:222px;width:96px;text-align:center;
    font:400 15px/17px "Open Sans",sans-serif;color:#444;
  }
  .brand{position:absolute;left:560px;top:28px;width:487px;text-align:right;color:var(--ink)}
  .brand-name{display:block;font:400 76px/90px "Archivo Black",sans-serif;letter-spacing:-2px}
  .brand-sub{display:block;font:400 44px/56px "Archivo Black",sans-serif;margin-right:20px}
  .benefits{position:absolute;left:456px;top:214px;list-style:none}
  .benefits li{display:flex;align-items:center;height:48px;
    font:700 34px/1 "Open Sans",sans-serif;color:var(--ink);letter-spacing:-.3px}
  .benefits svg{width:36px;height:36px;margin-right:15px;flex:none}
  .dates{position:absolute;left:531px;top:390px;white-space:nowrap;
    font:600 56px/1 "Oswald",sans-serif;color:var(--red);letter-spacing:-1.5px}
  .only{position:absolute;left:564px;top:458px;font:400 52px/1 "Archivo Black",sans-serif;color:var(--ink);letter-spacing:2px}
  .price{position:absolute;left:532px;top:508px;white-space:nowrap;
    font:400 190px/1 "Anton",sans-serif;color:var(--red);
    text-shadow:5px 5px 0 var(--ink);letter-spacing:2px}
  .cents{position:absolute;left:877px;top:526px;font:400 100px/1 "Anton",sans-serif;color:var(--red);
    text-shadow:4px 4px 0 var(--ink)}
  .disclaimer{position:absolute;left:567px;top:724px;white-space:nowrap;
    font:600 italic 17px/1 "Open Sans",sans-serif;color:var(--grey)}
  .band{position:absolute;left:0;top:761px;width:1120px;height:106px;background:var(--band);
    display:flex;align-items:center;justify-content:center}
  .band p{white-space:nowrap;font:600 italic 50px/1 "Fira Sans Extra Condensed",sans-serif;color:#fff;letter-spacing:-.5px}
</style>
</head>
<body>
<main class="postcard">
  <svg class="swoosh" viewBox="0 0 1120 867" aria-hidden="true">
    <defs>
      <linearGradient id="wave" x1="0" y1="0" x2="1" y2="0">
        <stop offset="0" stop-color="#ffffff" stop-opacity="0"/>
        <stop offset=".5" stop-color="#7cc0ec" stop-opacity=".7"/>
        <stop offset="1" stop-color="#3a9ee0" stop-opacity=".9"/>
      </linearGradient>
    </defs>
    <path d="M300 760 C560 700 720 520 1120 300 L1120 460 C860 560 640 700 420 761 Z" fill="url(#wave)"/>
    <path d="M560 761 C760 640 920 520 1120 470 L1120 761 Z" fill="#a9d8f5" opacity=".7"/>
    <path d="M250 700 C520 620 760 420 1120 250" fill="none" stroke="#ffffff" stroke-width="6" opacity=".8"/>
  </svg>

  <div class="photo" role="img" aria-label="Photo of a technician in uniform and cap standing beside an air conditioning unit"></div>

  <div class="badge">
    <svg viewBox="0 0 333 331" width="333" height="331" aria-hidden="true">
      <defs>
        <linearGradient id="silverFill" x1="0" y1="0" x2="1" y2="1">
          <stop offset="0" stop-color="#ffffff"/><stop offset="1" stop-color="#cfcfcf"/>
        </linearGradient>
      </defs>
      <path d="M4 0 H329 L175 326 Q166 338 157 326 Z" fill="#9e9e9e"/>
      <path d="M8 0 H322 L172 316 Q166 326 160 316 Z" fill="url(#silverFill)"/>
      <path d="M22 6 H308 L166 300 Z" fill="none" stroke="#555" stroke-width="2" stroke-dasharray="8 6"/>
      <path d="M44 133 H286 L280 217 H50 Z" fill="var(--ribbon)"/>
      <path d="M156 258 H178 L167 280 Z" fill="var(--ribbon)"/>
    </svg>
    <div class="badge-title">Heating &amp;<br>Cooling</div>
    <div class="badge-ribbon">BEST OFFER</div>
    <div class="badge-note">special<br>price</div>
  </div>

  <div class="brand">
    <span class="brand-name">Brightvale</span>
    <span class="brand-sub">Tune-Up</span>
  </div>

  <ul class="benefits">
    <li><svg viewBox="0 0 36 36"><rect width="36" height="36" rx="6" fill="var(--tick)"/><path d="M9 18 L15 24 L27 11" fill="none" stroke="#fff" stroke-width="4" stroke-linecap="round" stroke-linejoin="round"/></svg>Lower Energy Bills</li>
    <li><svg viewBox="0 0 36 36"><rect width="36" height="36" rx="6" fill="var(--tick)"/><path d="M9 18 L15 24 L27 11" fill="none" stroke="#fff" stroke-width="4" stroke-linecap="round" stroke-linejoin="round"/></svg>Increase the life of your system</li>
    <li><svg viewBox="0 0 36 36"><rect width="36" height="36" rx="6" fill="var(--tick)"/><path d="M9 18 L15 24 L27 11" fill="none" stroke="#fff" stroke-width="4" stroke-linecap="round" stroke-linejoin="round"/></svg>Prevent future breakdowns</li>
  </ul>

  <p class="dates">April 1st - June 31st.</p>
  <p class="only">Only</p>
  <p class="price">$99</p>
  <p class="cents">00</p>
  <p class="disclaimer">Does not cover repair or parts</p>

  <footer class="band"><p>Stay Cool this Summer with our Brightvale Tune Up Program</p></footer>
</main>
</body>
</html>
```